Business Card Ayurvedic Massage

I'm starting with my ayurvedic massage business and need a business card design. The design should be inline with my brand/logo as well as with the design of my website (www.lumo-thara.ch).
Front: logo and text "Ayurvedische Massagen"
back: name and adress (see details https://www.lumo-thara.ch/kontakt.html)

```html
<!DOCTYPE html>
<html lang="de">
<head>
<meta charset="utf-8">
<title>Lumo-Thara – Visitenkarten</title>
<link href="https://fonts.googleapis.com/css2?family=Libre+Baskerville:ital,wght@0,400;0,700;1,400&display=swap" rel="stylesheet">
<style>
  :root {
    --page-bg: #2f2f2f;
    --card-red: #8e0f16;
    --card-red-light: #a8161e;
    --card-red-dark: #6a0a10;
    --band-red: #7a0c12;
    --gold: #e0b24a;
    --gold-light: #f3d27a;
    --gold-dark: #a87a22;
    --ivory: #f7efe2;
    --serif: "Libre Baskerville", "Times New Roman", serif;
  }
  * { margin: 0; padding: 0; box-sizing: border-box; }
  html, body { width: 1200px; height: 1021px; overflow: hidden; background: var(--page-bg); }
  .canvas {
    position: relative; width: 1200px; height: 1021px;
    display: flex; flex-direction: column; align-items: center; justify-content: center; gap: 40px;
    font-family: var(--serif);
  }
  .card {
    position: relative; width: 760px; height: 440px; overflow: hidden;
    background: radial-gradient(ellipse at 50% 35%, var(--card-red-light) 0%, var(--card-red) 55%, var(--card-red-dark) 100%);
    box-shadow: 0 10px 28px rgba(0,0,0,.45);
  }
  .card__scenery {
    position: absolute; left: 0; right: 0; top: 70px; height: 280px;
    background: linear-gradient(180deg, rgba(90,6,10,0) 0%, rgba(90,6,10,.35) 70%, rgba(90,6,10,.15) 100%);
  }
  .card__band {
    position: absolute; left: 0; right: 0; bottom: 0;
    background: var(--band-red);
    border-top: 2px solid var(--gold);
  }
  .front .card__band { height: 110px; }
  .back .card__band { height: 95px; }
  .elephant {
    position: absolute; width: 160px; height: 150px;
    border-radius: 40% 40% 18% 18%;
    background: radial-gradient(ellipse at 50% 45%, var(--gold-light) 0%, var(--gold) 45%, #b3361e 100%);
    opacity: .92;
  }
  .brand {
    position: absolute; left: 0; right: 0; text-align: center;
    color: var(--gold); font-weight: 700; font-size: 40px; letter-spacing: 2px;
  }
  .tagline {
    position: absolute; left: 0; right: 0; text-align: center;
    color: var(--gold-light); font-size: 21px; letter-spacing: .5px;
  }
  .front .elephant--left { left: 70px; top: 55px; }
  .front .elephant--right { right: 60px; top: 160px; }
  .front .brand { top: 185px; }
  .front .tagline { top: 245px; }
  .ornament {
    position: absolute; left: 50%; top: 312px; width: 36px; height: 36px; margin-left: -18px;
    border-radius: 50%; border: 2px dotted var(--gold); background: var(--band-red);
  }
  .front .website {
    position: absolute; left: 0; right: 0; top: 375px; text-align: center;
    color: var(--gold); font-size: 19px; letter-spacing: 3px;
  }
  .back .elephant--left { left: 55px; top: 30px; }
  .back .elephant--right { right: 50px; top: 125px; }
  .back .brand { top: 130px; font-size: 38px; }
  .back .tagline { top: 184px; font-size: 20px; }
  .person { position: absolute; left: 0; right: 0; top: 222px; text-align: center; }
  .person__name { color: var(--gold); font-size: 25px; font-weight: 700; line-height: 1.2; }
  .person__role { color: var(--ivory); font-size: 14px; margin-top: 2px; }
  .address {
    position: absolute; left: 0; right: 0; top: 292px; text-align: center;
    color: var(--ivory); font-size: 15px; line-height: 1.2;
  }
  .contacts {
    position: absolute; left: 0; right: 0; top: 326px;
    display: flex; justify-content: space-around; padding: 0 40px;
  }
  .contact { display: flex; flex-direction: column; align-items: center; gap: 12px; }
  .contact__icon {
    width: 38px; height: 38px; border-radius: 50%;
    background: radial-gradient(circle, var(--gold-light) 0%, var(--gold) 60%, var(--gold-dark) 100%);
    border: 2px dotted var(--gold-light);
    display: flex; align-items: center; justify-content: center;
  }
  .contact__text { color: var(--gold); font-size: 17px; }
</style>
</head>
<body>
<main class="canvas">

  <section class="card front" aria-label="Vorderseite">
    <div class="card__scenery" role="img" aria-label="Blasse Silhouette eines indischen Palastes mit Zypressen"></div>
    <div class="card__band"></div>
    <div class="elephant elephant--left" role="img" aria-label="Geschmückter goldener Elefant mit Schirm"></div>
    <div class="elephant elephant--right" role="img" aria-label="Geschmückter goldener Elefant mit Schirm"></div>
    <div class="brand">lumo-thara</div>
    <div class="tagline">Ayurvedische Massagen</div>
    <div class="ornament"></div>
    <div class="website">www.lumo-thara.ch</div>
  </section>

  <section class="card back" aria-label="Rückseite">
    <div class="card__scenery" role="img" aria-label="Blasse Silhouette eines indischen Palastes mit Zypressen"></div>
    <div class="card__band"></div>
    <div class="elephant elephant--left" role="img" aria-label="Geschmückter goldener Elefant mit Schirm"></div>
    <div class="elephant elephant--right" role="img" aria-label="Geschmückter goldener Elefant mit Schirm"></div>
    <div class="brand">lumo-thara</div>
    <div class="tagline">Ayurvedische Massagen</div>
    <div class="person">
      <div class="person__name">Daniel Hartmann</div>
      <div class="person__role">President</div>
    </div>
    <div class="address">Mira Berlauer, lumo-thara, Lindenweg 14, 8867 Seewilen (SZ)</div>
    <div class="contacts">
      <div class="contact">
        <span class="contact__icon">
          <svg width="20" height="14" viewBox="0 0 20 14"><rect x="1" y="1" width="18" height="12" fill="none" stroke="#6a0a10" stroke-width="1.6"/><path d="M1 1 L10 8 L19 1" fill="none" stroke="#6a0a10" stroke-width="1.6"/></svg>
        </span>
        <span class="contact__text">info@lumo-thara.ch</span>
      </div>
      <div class="contact">
        <span class="contact__icon">
          <svg width="14" height="20" viewBox="0 0 14 20"><rect x="1.5" y="1" width="11" height="18" rx="2" fill="none" stroke="#6a0a10" stroke-width="1.6"/><circle cx="7" cy="16" r="1" fill="#6a0a10"/></svg>
        </span>
        <span class="contact__text">+41 77 318 40 26</span>
      </div>
      <div class="contact">
        <span class="contact__icon">
          <svg width="20" height="20" viewBox="0 0 20 20"><circle cx="10" cy="10" r="8" fill="none" stroke="#6a0a10" stroke-width="1.6"/><ellipse cx="10" cy="10" rx="3.5" ry="8" fill="none" stroke="#6a0a10" stroke-width="1.4"/><path d="M2 10 H18" stroke="#6a0a10" stroke-width="1.4"/></svg>
        </span>
        <span class="contact__text">www.lumo-thara.ch</span>
      </div>
    </div>
  </section>

</main>
</body>
</html>
```